Web Design Project

I have a website which looks dull and uninteresting. I'd like to apply a fresh and clean look to it, which better reflects the quality of the service I sell.The website address is http://www.brightquillpages.co.uk.

Target Market(s)

Financial advisers (financially sophisticated individuals)

Industry/Entity Type

It Service

Requirements
Should not have
• Please do not use obvious but irrelevant and boring imagery such as banks, pages from the DL, money, books or libraries. Prefer slick relevant graphics and crisp typography.

```html
<!DOCTYPE html>
<html lang="en">
<head>
<meta charset="utf-8">
<title>Bright Quill Pages</title>
<link href="https://fonts.googleapis.com/css2?family=Arimo:wght@400;700&family=Open+Sans:wght@400;600&display=swap" rel="stylesheet">
<style>
:root{
  --red:#c4271d;
  --tab-grey:#8c8c8c;
  --tab-dark:#2a2a2a;
  --band:#e4e4e4;
  --ink:#222;
  --muted:#a8a8a8;
  --mid:#6a6a6a;
  --panel:#dcdcdc;
  --footer:#0c0c0c;
  --footer-base:#1b1b1b;
  --white:#fff;
}
*{box-sizing:border-box;margin:0;padding:0}
html,body{width:1151px;height:1200px;overflow:hidden;background:var(--white)}
body{position:relative;font-family:'Arimo',Arial,sans-serif;color:var(--ink)}
.nav{position:absolute;top:0;left:0;width:1151px;height:56px;background:var(--white)}
.tab{position:absolute;top:6px;height:50px;width:150px;display:flex;align-items:center;justify-content:center;
  color:var(--white);font-weight:700;font-size:15px;
  clip-path:polygon(8% 0,92% 0,100% 100%,0 100%);
  background:linear-gradient(#a9a9a9,#7b7b7b)}
.tab.is-home{background:linear-gradient(#d83a2d,#a81c13)}
.tab.is-dark{background:linear-gradient(#444,#111)}
.header{position:absolute;top:56px;left:0;width:1151px;height:222px;background:linear-gradient(#ececec,#dedede)}
.brand{position:absolute;left:44px;top:16px;font-size:52px;font-weight:700;color:var(--red);letter-spacing:-1px}
.tagline{position:absolute;left:158px;top:78px;font-size:25px;font-weight:700;color:#555}
.price{position:absolute;left:42px;top:113px;font-size:58px;color:var(--red)}
.offer{position:absolute;left:157px;top:120px;width:460px;font-size:13.5px;line-height:17px;color:var(--muted)}
.team-art{position:absolute;left:740px;top:20px;width:354px;height:176px}
.rule{position:absolute;left:60px;top:308px;width:1030px;height:4px;background:radial-gradient(ellipse at center,#bbb,transparent 70%)}
.profile{position:absolute;left:992px;top:291px;font-size:14px;color:#444;display:flex;align-items:center;gap:3px}
.profile i{display:inline-block;width:14px;height:14px;background:#2f5ea0}
.copy{position:absolute;left:44px;top:356px;width:616px;font-family:'Open Sans',Arial,sans-serif;font-size:15.6px;line-height:20.8px;color:var(--ink)}
.library{position:absolute;left:20px;top:786px;width:620px;height:76px;border-radius:8px;background:linear-gradient(#eee,#d6d6d6);
  box-shadow:0 2px 4px rgba(0,0,0,.25);text-align:center;font-size:13px;line-height:19px;color:#555;padding-top:9px}
.library strong{color:var(--red)}
.side{position:absolute;left:687px;top:358px;width:454px;height:548px;background:var(--panel);border-radius:30px 0 0 30px}
.login{position:absolute;left:55px;top:22px;width:390px;font-size:14px;color:#444}
.login p{margin-bottom:8px}
.field{display:flex;justify-content:space-between;align-items:center;height:22px;margin-bottom:6px}
.field span.box{width:180px;height:17px;background:var(--white);border:1px solid #999}
.btn{margin-left:auto;width:52px;height:16px;background:#111;color:var(--white);font-size:12px;font-weight:700;text-align:center;line-height:16px}
.articles{position:absolute;left:20px;top:130px;width:434px;height:412px;background:var(--white);border-radius:18px 0 0 18px;
  padding:10px 14px;font-size:12px;line-height:14.6px;color:#9a9a9a}
.articles h3{font-size:12px;color:#222;font-weight:700}
.articles .gap{margin-top:12px}
.footer{position:absolute;top:937px;left:0;width:1151px;height:263px;background:var(--footer)}
.piece{position:absolute;width:96px;height:70px;background:#b9b9b9;border-radius:6px;color:var(--white);font-size:10px;line-height:12px;padding:14px 0 0 10px}
.piece.dark{background:#555}
.guides{position:absolute;left:291px;top:8px;color:var(--white);font-size:27px;font-weight:700}
.guides-sub{position:absolute;left:291px;top:48px;color:#ccc;font-size:13px;font-weight:700}
.links{position:absolute;top:8px;list-style:none;color:#ddd;font-size:13.5px;line-height:18px}
.links li::before{content:"• ";color:var(--red)}
.social{position:absolute;left:1030px;top:165px;display:flex;gap:12px}
.social i{width:22px;height:22px;display:block}
.base{position:absolute;left:0;top:202px;width:1151px;height:61px;background:var(--footer-base);color:#ccc;font-size:12px}
.base .c{position:absolute;left:44px;top:24px}
.base .r{position:absolute;left:983px;top:24px}
</style>
</head>
<body>
<nav class="nav">
  <div class="tab is-home" style="left:16px">Home</div>
  <div class="tab" style="left:152px">A-Z Articles</div>
  <div class="tab" style="left:284px">Inheritance Tax</div>
  <div class="tab" style="left:425px">Insurances</div>
  <div class="tab" style="left:564px">Morgages</div>
  <div class="tab is-dark" style="left:706px">Other</div>
  <div class="tab is-dark" style="left:848px">Retirement</div>
  <div class="tab is-dark" style="left:988px;width:150px;font-size:14px">Saving&amp;Investment</div>
</nav>

<header class="header">
  <div class="brand">BrightQuillPages.co.uk</div>
  <div class="tagline">Words to use as you please</div>
  <div class="price">£49</div>
  <p class="offer">Unlimited acces to all our articles for just one price.<br>Use our articles and guides as you want, for as long as you want - including new material as it's added - for £49 + VAT a year.</p>
  <div class="team-art" role="img" aria-label="Business people silhouettes above coloured jigsaw pieces with finance icons"
       style="background:linear-gradient(180deg,#c9c9c9 0%,#e0e0e0 45%,#d65a2a 55%,#c33a8c 65%,#3a79c8 78%,#22a0a0 88%,#4aa341 100%);opacity:.85"></div>
</header>

<div class="rule"></div>
<div class="profile">Network <i></i> profile</div>

<main class="copy">
<p>Cras neque justo, ultrices at, rhoncus a facilisis eget,nisl. Quisque vitae pede. Nam et augue. Sed a elit. Ut vel massa. Suspendisse nibh pede, ultrices vitae, ultrices nec, mollis non nibh. In sit amet pede quis leo vulputate hendrerit. Cras laoreet leo et justo auctor condimentum. Integer id enim. Suspendisse nibh pede, ultrices vitae, ultrices nec, mollis non, nibh. In sit amet pede quis leo vulputate hendrerit.Cras neque justo, ultrices at, rhoncus a facilisis eget,nisl. Quisque vitae pede. Nam et augue.</p>
<p>Sed a elit. Ut vel massa. Suspendisse nibh pede, ultrices vitae, ultrices nec, mollis non nibh. In sit amet pede quis leo vulputate hendrerit.</p>
<p>Cras neque justo, ultrices at, rhoncus a facilisis eget,nisl. Quisque vitae pede. Nam et augue. Sed a elit. Ut vel massa. Suspendisse nibh pede, ultrices vitae, ultrices nec, mollis non nibh. In sit amet pede quis leo vulputate hendrerit. Cras laoreet leo et justo auctor condimentum. Integer id enim. Suspendisse nibh pede, ultrices vitae, ultrices nec, mollis non, nibh. In sit amet pede quis leo vulputate hendrerit.Cras neque justo, ultrices at, rhoncus a facilisis eget,nisl. Quisque vitae pede. Nam et augue.</p>
<p>Sed a elit. Ut vel massa. Suspendisse nibh pede, ultrices vitae, ultrices nec, mollis non nibh. In sit amet pede quis leo vulputate hendrerit.</p>
</main>

<div class="library">
  To view our library follow this link. To see samples of the articles go here.<br>
  <strong>£49 a year, at least 131 articles (plus free guide as they're published)</strong><br>
  follow this link to have full acces to the library.
</div>

<aside class="side">
  <div class="login">
    <p>Member: Please enter your email address and password</p>
    <div class="field">Email Address: <span class="box"></span></div>
    <div class="field">Password: <span class="box"></span></div>
    <div class="btn">Login</div>
  </div>
  <div class="articles">
    <div>Futures and Options on MarketPath units<br>trusts and OEICS are categorised Money.<br>LaunderingQRPSStamp Duty Reserve Tax<br>The Financial Conduct Board (FCB)</div>
    <h3>Articles Added in November 2010 <span style="font-weight:400;color:#aaa">--&gt;</span></h3>
    <div>Self Select ISAThe Lifetime Allowance and<br>The Annual Allowance.</div>
    <h3 class="gap">Articles added in June 2011:</h3>
    <div>Fundamental Analysis and Key Ratios<br>Inheritance Tax Planning and Equity Release<br>Inheritance Tax Planning and Qualifying Investments<br>Inheritance Tax Planning and Taper Relief<br>Inheritance Tax Planning and The bare and Basic Essentials<br>Inheritance Tax Planning Overview<br>Margin Of Safety<br>Broadline 1000 Index (The)</div>
    <h3 class="gap">Articles added in June 2011:</h3>
    <div>Inheritance Tax Planning and Life Assurance Policies<br>Inheritance Tax Planning and Loan Trusts<br>Inheritance Tax Planning and Spousal Bypass Trusts<br>Inheritance Tax Planning and The Spouse or Civil Partner Exemtion<br>Inheritance Tax Planning Interests in Possession Trusts<br>Inheritance Tax Planning and Types of Trusts<br>Inheritance Tax Planning Valuing an Estate for IHT purposes<br>Standard 500 Index (The)</div>
  </div>
</aside>

<footer class="footer">
  <div class="piece" style="left:30px;top:14px">Why financial advice can never be free</div>
  <div class="piece dark" style="left:156px;top:14px">What takes to be a financial adviser</div>
  <div class="piece" style="left:30px;top:112px;height:74px;padding-top:20px">IHT planning, a guessing and waiting game.</div>
  <div class="guides">Chek out my Two Free Guides</div>
  <div class="guides-sub">The bare and basic IHT planning essentials for your clients...</div>
  <ul class="links" style="left:732px">
    <li>Home</li><li>Samples</li><li>The people who write the articles</li><li>Please don't lift our words</li><li>A-Z of articles</li><li>Enter the library</li><li>Join the library here</li>
  </ul>
  <ul class="links" style="left:956px">
    <li>Some FAQs</li><li>Contact us</li><li>A few terms &amp; Conditions</li><li>Forgotten your password?</li><li>A comment to make?</li><li>A question to ask?</li><li>What something writing?</li>
  </ul>
  <div class="social"><i style="background:#3b5a9a"></i><i style="background:#3aa6d8"></i><i style="background:#e57a1c"></i></div>
  <div class="base"><span class="c">Copyright ©Bright Quill Pages 2011.</span><span class="r">Site Map &nbsp;|&nbsp; Privacy Policy</span></div>
</footer>
</body>
</html>
```